Vela Korrindo SOLD Post Card directed to luxury market.

Vibrant colors that stand out and easy to read fonts.

JUST SOLD within 3 days with multiple offers at 4157 Vela Korrindo Drive, Granite Bay, CA 95746

When working with sellers I get involved with staging, professional photography, renovations so that the property showcases it's best features. Seasoned Realtor, Knowledgeable of the Area, Determine to get top Dollar for your property.
Licensed since 1991. Call Marisa Quenby direct @ 916-555-0173

NOTE to Designers: I would like to utilize the same post card for all of my SOLD properties. I would like to have the ability to edit the card and upload photo's.

Target Market(s)

Luxury Homes

Colors
0255a3
00a990
fbed22

Requirements
Must have
• Back of Post Card:
• Marisa Quenby, Broker CALBRE#04728351
• Tarnwell Homes Group
• 2385 Heron Ridge Court
• Roseville, CA 95747
• MUST have for EDDM Retail postage on the back in a small box:
• PRSRT STD
• ECRWSS
• U.S. Postage Paid
• EDDM Retail
• Local Postal Customer
• Add email address: marisa@dialTKSrealty.example
Nice to have
• Images of luxury - very distinctive looking.
Should not have
• Too busy.

```html
<!DOCTYPE html>
<html lang="en">
<head>
<meta charset="utf-8">
<title>Just Sold Postcard – Marisa Quenby</title>
<link rel="stylesheet" href="https://fonts.googleapis.com/css2?family=Roboto:wght@400;700;900&family=Great+Vibes&family=Cinzel:wght@400;600&family=Libre+Baskerville&display=swap">
<style>
  :root{
    --navy:#1d2f6a;
    --blue:#0255a3;
    --green:#7aa83c;
    --teal:#00a990;
    --yellow:#fbed22;
    --silver-light:#f1f1f1;
    --silver-dark:#b9bcc0;
    --ink:#333a44;
    --white:#ffffff;
  }
  *{box-sizing:border-box;margin:0;padding:0}
  html,body{width:774px;height:1200px;overflow:hidden;background:var(--white)}
  .postcard{position:relative;width:774px;height:1200px;font-family:"Roboto",Arial,sans-serif;color:var(--ink)}
  .side{position:absolute;left:0;width:774px;height:600px;overflow:hidden;background:var(--white)}
  .front{top:0}
  .back{top:600px;border-top:2px solid #e3e3e3}
  .abs{position:absolute}
  .shapes{position:absolute;left:0;top:0}

  /* front */
  .sold-band{left:14px;top:24px;width:140px;height:400px;background:linear-gradient(90deg,var(--silver-dark),var(--silver-light) 55%,var(--silver-dark))}
  .sold-title{left:-110px;top:170px;width:360px;transform:rotate(-90deg);text-align:center;font-family:"Great Vibes",cursive;font-size:84px;color:var(--navy);line-height:1}
  .sold-sub{left:120px;top:340px;width:260px;transform:rotate(-90deg);transform-origin:left top;font-size:14px;color:var(--navy)}
  .agent-name{left:175px;top:12px;font-size:36px;font-weight:700;color:var(--green)}
  .agent-phone{left:175px;top:54px;font-size:31px;font-weight:700;color:var(--navy)}
  .agent-email{left:175px;top:94px;font-size:16px;color:var(--navy)}
  .brand{display:flex;align-items:center;gap:8px;white-space:nowrap;font-family:"Roboto",Arial,sans-serif;font-weight:700;color:var(--navy)}
  .brand-dot{width:20px;height:20px;border-radius:50%;background:var(--green);flex:none}
  .front .brand{left:526px;top:56px;font-size:20px}
  .photo{position:absolute;border:4px solid var(--white)}
  .photo-main{left:170px;top:112px;width:604px;height:320px;border:none;background:linear-gradient(180deg,#8fb3d6 0%,#a7b7a0 35%,#9c5c3c 55%,#6d6a55 75%,#8c8676 100%)}
  .photo-pool{left:552px;top:292px;width:212px;height:132px;background:linear-gradient(180deg,#7c8f5a,#3fa6c8 60%,#c9b79a)}
  .photo-garden{left:470px;top:382px;width:150px;height:148px;background:linear-gradient(180deg,#5c7a3e,#9a7b55 55%,#4aa6c4)}
  .photo-patio{left:628px;top:436px;width:136px;height:132px;background:linear-gradient(180deg,#6f8a4a,#b9956a 60%,#7b6a52)}
  .address{left:175px;top:452px;color:var(--white);font-size:20px;line-height:1.3}
  .badge{width:14px;height:14px;background:var(--white);top:572px}

  /* back */
  .back .brand{left:40px;top:52px;font-size:18px}
  .return-address{left:72px;top:84px;font-size:12px;line-height:1.35;color:var(--navy)}
  .postal-box{border:1.5px solid var(--ink);top:30px;height:118px;font-family:"Roboto",Arial,sans-serif}
  .recipient{left:418px;width:190px;padding:14px 16px;font-size:18px;line-height:1.35;color:var(--ink)}
  .indicia{left:622px;width:140px;padding:14px 6px;text-align:center;font-size:14px;font-weight:700;line-height:1.45;color:var(--ink)}
  .pitch{left:50px;top:180px;width:674px;text-align:center;font-family:"Cinzel",serif;font-size:25px;line-height:1.28;color:var(--blue);text-transform:uppercase}
  .highlights{left:36px;top:428px;list-style:none;font-family:"Libre Baskerville",serif;font-size:15px;line-height:1.45;color:var(--white)}
  .highlights li::before{content:"• ";}
  .call{left:60px;top:526px;font-family:"Libre Baskerville",serif;color:var(--white);text-transform:uppercase;font-size:20px;line-height:1.35}
  .agent-photo{left:588px;top:436px;width:150px;height:145px;border:4px solid var(--white);background:linear-gradient(180deg,#c8d3dc,#e6c9a8 55%,#c79a74)}
</style>
</head>
<body>
<div class="postcard">

  <section class="side front">
    <svg class="shapes" width="774" height="600" viewBox="0 0 774 600" aria-hidden="true">
      <path d="M720 150 C760 200 774 260 774 300 L774 430 L720 430 Z" fill="var(--green)"/>
      <path d="M0 455 C200 420 420 440 774 390 L774 600 L0 600 Z" fill="var(--green)"/>
      <path d="M0 470 C200 440 420 455 774 410 L774 600 L0 600 Z" fill="var(--navy)"/>
    </svg>
    <div class="abs sold-band"></div>
    <div class="abs sold-title">Just Sold</div>
    <div class="abs sold-sub">with multiple offers</div>

    <div class="abs agent-name">Marisa Quenby</div>
    <div class="abs agent-phone">916-555-0173</div>
    <div class="abs agent-email">marisa@dialTKSrealty.example</div>
    <div class="abs brand"><span class="brand-dot"></span>Tarnwell Homes Group</div>

    <div class="photo photo-main" role="img" aria-label="Photo of the sold ranch-style home with stone facade, oak tree and boulders"></div>
    <div class="photo photo-pool" role="img" aria-label="Photo of the backyard pool and spa"></div>
    <div class="photo photo-garden" role="img" aria-label="Photo of the landscaped garden and pool area"></div>
    <div class="photo photo-patio" role="img" aria-label="Photo of the rear patio"></div>

    <div class="abs address">4157 Vela Korrindo Drive<br>Granite Bay, CA 95746</div>
    <div class="abs badge" style="left:718px"></div>
    <div class="abs badge" style="left:740px"></div>
  </section>

  <section class="side back">
    <svg class="shapes" width="774" height="600" viewBox="0 0 774 600" aria-hidden="true">
      <path d="M0 380 C250 420 520 350 774 400 L774 600 L0 600 Z" fill="var(--green)"/>
      <path d="M0 405 C250 440 520 375 774 420 L774 600 L0 600 Z" fill="var(--navy)"/>
    </svg>
    <div class="abs brand"><span class="brand-dot"></span>Tarnwell Homes Group</div>
    <div class="abs return-address">2385 Heron Ridge Court<br>Roseville, CA 95747</div>

    <div class="abs postal-box recipient">Local<br>Postal Customer</div>
    <div class="abs postal-box indicia">PRSRT STD<br>ECRWSS<br>U.S. POSTAGE<br>PAID<br>EDDM RETAIL</div>

    <p class="abs pitch">When working with sellers I assist with staging, professional photography and selecting renovation or repair specialists so that the best features of your property are showcased.</p>

    <ul class="abs highlights">
      <li>Seasoned Realtor since 1991, CALBRE#04728351</li>
      <li>Extensive Knowledge of the Area and market</li>
      <li>Determined to get top Dollar for your property</li>
    </ul>
    <div class="abs call">Call Marisa Quenby<br>• Direct @ 916-555-0173</div>

    <div class="abs agent-photo" role="img" aria-label="Portrait photo of agent Marisa Quenby"></div>
  </section>

</div>
</body>
</html>
```